Transformative School Model Needs a Website. I am easy to work with.

Greetings:
I am creating a K-12 school that is a complete and total re-imagination of what education can be for children, families, communities, and the planet. While we will begin as a K-12 school, I really see it as a complete life cycle education (birth to death). I'm looking for a website to describe my new transformational educational model. I anticipate having 7-8 pages. I have all the copy ready.
I am the Founder. I am easy to work with, an effective communicator, and I’m very good at knowing what I want and providing specific and concrete detail, examples, and direction to make sure I use your time wisely.

```html
<!DOCTYPE html>
<html lang="en">
<head>
<meta charset="utf-8">
<title>Evergreen Unity School</title>
<link href="https://fonts.googleapis.com/css2?family=Outfit:wght@400;500;600;700&display=swap" rel="stylesheet">
<style>
:root{
  --orange:#f57c14;
  --blue:#1b4fb7;
  --blue-dark:#153f96;
  --navy:#0e1b2c;
  --soft:#eef1f6;
  --ink:#1b1b1f;
  --text:#4a4d55;
  --white:#ffffff;
  --btn-soft:#e7ecf6;
}
*{box-sizing:border-box;margin:0;padding:0}
html,body{width:1200px;height:5204px;overflow:hidden}
body{font-family:"Outfit",sans-serif;color:var(--ink);background:var(--white);position:relative}
.abs{position:absolute}
section,header,footer,nav.nav{position:absolute;left:0;width:1200px}
.underline{display:block;width:34px;height:4px;background:var(--orange);border-radius:2px}
.btn{display:inline-flex;align-items:center;gap:8px;font-weight:600;font-size:15px;border-radius:4px;padding:0 26px;height:52px;text-decoration:none}
.btn-blue{background:var(--blue);color:var(--white)}
.btn-soft{background:var(--btn-soft);color:var(--blue);height:46px;font-size:14px}
.btn-orange{background:var(--orange);color:var(--white);height:48px;font-size:14px}
.arrow-ic{width:16px;height:16px}
p{line-height:1.75}

/* top bar */
.topbar{top:0;height:46px;background:var(--orange);color:var(--white);font-size:15px;z-index:1}
.topbar .item{position:absolute;top:13px;display:flex;align-items:center;gap:8px}
.topbar .social{position:absolute;top:15px;display:flex;gap:16px;left:1020px}
.dot{width:14px;height:14px;border:2px solid var(--white);border-radius:50%;display:inline-block}
.social .sq{width:12px;height:14px;background:var(--white);border-radius:2px}
.divider{position:absolute;left:986px;top:14px;width:1px;height:18px;background:rgba(255,255,255,.6)}

/* nav */
.nav{top:46px;height:80px;background:var(--white);z-index:5}
.brand{position:absolute;left:96px;top:-38px;width:150px;height:150px;border-radius:50%;background:var(--white);box-shadow:0 4px 14px rgba(0,0,0,.12);display:flex;align-items:center;justify-content:center;text-align:center;font-weight:600;font-size:16px;line-height:1.2;color:var(--ink)}
.brand span{width:116px;height:116px;border-radius:50%;border:2px solid var(--ink);display:flex;align-items:center;justify-content:center;padding:10px}
.menu{position:absolute;left:304px;top:30px;display:flex;gap:27px;font-size:15px;font-weight:500}
.menu a{color:var(--ink);text-decoration:none}
.menu a.active{color:var(--orange)}

/* hero */
.hero{top:126px;height:562px;background:linear-gradient(90deg,#4e5a3a 0%,#6f7a55 45%,#a39070 70%,#6b6147 100%)}
.hero-title{position:absolute;left:90px;top:92px;color:var(--white);font-size:60px;font-weight:700;line-height:1.12}
.hero-swoosh{position:absolute;left:320px;top:222px}
.hero-text{position:absolute;left:90px;top:312px;width:430px;color:var(--white);font-size:16px;line-height:1.8}
.hero .btn{position:absolute;left:90px;top:404px;height:52px;font-size:15px}
.slider{position:absolute;left:554px;top:512px;display:flex;align-items:center;gap:10px;color:var(--white)}
.slider i{width:6px;height:6px;border-radius:50%;background:rgba(255,255,255,.6);display:block}
.slider i.on{background:var(--white);width:8px;height:8px}

/* spiritual */
.spirit{top:688px;height:608px;background:var(--soft);z-index:2}
.spirit h2{position:absolute;left:92px;top:132px;font-size:36px;font-weight:600}
.spirit .underline{position:absolute;left:92px;top:184px}
.spirit p{position:absolute;left:92px;top:214px;width:492px;font-size:15.5px;color:var(--text);line-height:1.9}
.spirit .btn{position:absolute;left:92px;top:418px}
.spirit-art{position:absolute;left:710px;top:92px}
.down-btn{position:absolute;left:570px;width:60px;height:60px;border-radius:50%;background:var(--white);display:flex;align-items:center;justify-content:center;color:var(--blue);font-size:22px}

/* about */
.about{top:1296px;height:862px;background:var(--white)}
.about h2{position:absolute;left:0;width:1200px;text-align:center;top:120px;font-size:36px;font-weight:600}
.about .underline{position:absolute;left:583px;top:168px}
.about-text{position:absolute;left:600px;top:272px;width:496px;font-size:15.5px;color:var(--text);line-height:1.9}
.about-text p+p{margin-top:24px}
.checks{position:absolute;left:600px;top:528px;list-style:none;font-size:15.5px;color:var(--text)}
.checks li{display:flex;align-items:center;gap:18px;height:40px}
.about .btn{position:absolute;left:600px;top:666px}

/* purpose */
.purpose{top:2158px;height:1096px}
.purpose-band{position:absolute;left:0;top:0;width:1200px;height:542px;background:linear-gradient(180deg,#2457c0 0%,#1b4fb7 100%)}
.purpose h2{position:absolute;left:92px;top:92px;font-size:36px;font-weight:600;color:var(--white)}
.purpose .underline{position:absolute;left:92px;top:144px}
.purpose-lead{position:absolute;left:554px;top:92px;width:560px;color:var(--white);font-size:16px;line-height:1.8}
.card{position:absolute;width:326px;height:394px;background:var(--white);box-shadow:0 10px 30px rgba(20,40,80,.08);text-align:center}
.card svg.ic{position:absolute;left:131px;top:36px}
.card h3{position:absolute;left:0;width:100%;top:128px;font-size:20px;font-weight:600}
.card .underline{position:absolute;left:150px;top:162px;width:26px;height:3px}
.card p{position:absolute;left:28px;width:270px;top:188px;font-size:15.5px;color:var(--text);line-height:1.9}
.card .btn{position:absolute;left:82px;top:306px}
.donate{background:linear-gradient(135deg,#6f4a38 0%,#a0543d 45%,#3c3f52 100%);color:var(--white)}
.donate .badge{position:absolute;left:114px;top:36px;width:98px;height:98px;border-radius:50%;background:var(--white);display:flex;align-items:center;justify-content:center}
.donate h3{top:158px;font-size:29px;font-weight:700;line-height:1.35;color:var(--white)}
.donate .btn{left:76px;top:306px}
.corner{position:absolute;border:4px solid var(--white)}

/* statement */
.statement{top:3254px;height:710px}
.statement h2{position:absolute;left:0;width:1200px;text-align:center;top:48px;font-size:36px;font-weight:600}
.statement .underline{position:absolute;left:583px;top:98px}
.statement p{position:absolute;left:310px;width:580px;top:126px;text-align:center;font-size:16px;color:var(--text);line-height:1.85}
.rings{position:absolute;left:0;top:290px}

/* testimonials */
.reviews{top:3964px;height:804px;background:var(--soft)}
.reviews h2{position:absolute;left:92px;top:218px;font-size:36px;font-weight:600;line-height:1.2}
.reviews .underline{position:absolute;left:92px;top:314px}
.nav-arrows{position:absolute;left:970px;top:230px;display:flex;gap:18px}
.nav-arrows span{width:62px;height:62px;border-radius:50%;display:flex;align-items:center;justify-content:center}
.review{position:absolute;top:376px;width:494px;height:326px;background:var(--white)}
.review .avatar{position:absolute;left:44px;top:38px;width:80px;height:80px;border-radius:50%}
.review .quote{position:absolute;right:0;top:-16px}
.review p{position:absolute;left:44px;top:150px;width:420px;font-size:15.5px;color:var(--text);line-height:1.9}
.review .name{position:absolute;left:44px;top:254px;font-size:18px;color:var(--blue);font-weight:500}
.review .role{position:absolute;left:44px;top:282px;font-size:15px;color:var(--text)}

/* footer */
.footer{top:4768px;height:436px;background:var(--navy);color:var(--white)}
.foot-brand{position:absolute;left:112px;top:84px;width:130px;height:130px;border-radius:50%;border:2px solid var(--white);display:flex;align-items:center;justify-content:center;text-align:center;font-size:15px;font-weight:600;line-height:1.2;padding:16px}
.foot-social{position:absolute;left:92px;top:256px;display:flex;gap:12px}
.foot-social span{width:50px;height:50px;border-radius:50%;background:var(--orange);display:block}
.footer h4{position:absolute;top:80px;font-size:20px;font-weight:600}
.footer .underline{position:absolute;top:114px;width:30px;height:3px}
.links{position:absolute;top:148px;list-style:none;font-size:15px}
.links li{height:40px}
.contact{position:absolute;left:882px;font-size:15px;line-height:1.9}
.contact .ic{position:absolute;left:0;top:4px}
.contact div{padding-left:40px}
.copy{position:absolute;left:0;width:1200px;text-align:center;top:378px;font-size:14px;color:#9aa2b0}
</style>
</head>
<body>

<header class="topbar">
  <div class="item" style="left:392px"><span class="dot" style="border-radius:3px"></span>Email: hello@evergreenunity.org</div>
  <div class="item" style="left:738px">
    <svg width="16" height="16" viewBox="0 0 24 24" fill="none" stroke="#fff" stroke-width="2"><path d="M5 3h4l2 5-3 2a12 12 0 0 0 6 6l2-3 5 2v4a2 2 0 0 1-2 2A18 18 0 0 1 3 5a2 2 0 0 1 2-2z"/></svg>
    Call us: 123-456-7890</div>
  <span class="divider"></span>
  <div class="social" aria-label="Social links"><span class="sq"></span><span class="sq"></span><span class="sq"></span></div>
</header>

<nav class="nav">
  <div class="brand"><span>Evergreen Unity School</span></div>
  <div class="menu">
    <a class="active" href="#">About</a><a href="#">School Foundations</a><a href="#">Curriculum</a><a href="#">Pedagogy</a><a href="#">Outcomes</a><a href="#">Opening</a><a href="#">Testimonials</a><a href="#">Donate</a>
  </div>
</nav>

<section class="hero" role="img" aria-label="Photo of a smiling young boy leaning on a tree trunk outdoors">
  <h1 class="hero-title">Complete life<br>cycle education<br>system</h1>
  <svg class="hero-swoosh" width="180" height="20" viewBox="0 0 180 20"><path d="M4 16 Q90 -4 176 12" fill="none" stroke="var(--orange)" stroke-width="4" stroke-linecap="round"/></svg>
  <p class="hero-text">Lorem ipsum dolor sit ameto consectetur adipiscing elit sed do eiusmod tempor incididunt ut labore.</p>
  <a class="btn btn-blue" href="#">Go To School Foundation
    <svg class="arrow-ic" viewBox="0 0 16 16" fill="none" stroke="#fff" stroke-width="1.6"><circle cx="8" cy="8" r="7"/><path d="M5 8h6M8.5 5.5 11 8l-2.5 2.5"/></svg></a>
  <div class="slider"><span>&#8249;</span><i></i><i class="on"></i><i></i><span>&#8250;</span></div>
</section>

<section class="spirit">
  <h2>Spiritual philosophy</h2>
  <span class="underline"></span>
  <p>Lorem ipsum dolor sit ameto econsectetur adipisicing elit, sed do eiusmod tempor incididunt sedit ut labore et dolore magna aliqua. Ut enimosi ad minim veniam, quis nostrud exercitation ullamco laboris nisi ut aliquip exeai commodo consequat. Duis aute irure dolor in reprehenderit in voluptate velit esse cillum dolore eu fugiat nulla pariatur jantan seduis tem.</p>
  <a class="btn btn-blue" href="#">Read More
    <svg class="arrow-ic" viewBox="0 0 16 16" fill="none" stroke="#fff" stroke-width="1.6"><circle cx="8" cy="8" r="7"/><path d="M5 8h6M8.5 5.5 11 8l-2.5 2.5"/></svg></a>
  <svg class="spirit-art" width="400" height="420" viewBox="0 0 400 420">
    <path d="M28 105 A192 192 0 0 1 372 105" fill="none" stroke="var(--orange)" stroke-width="8"/>
    <path d="M32 310 A192 192 0 0 0 368 310" fill="none" stroke="var(--blue)" stroke-width="8"/>
    <circle cx="200" cy="200" r="192" fill="none" stroke="var(--blue)" stroke-width="2" stroke-dasharray="2 5"/>
    <defs><linearGradient id="meadow" x1="0" y1="0" x2="0" y2="1"><stop offset="0" stop-color="#c9b268"/><stop offset=".55" stop-color="#7f8d3c"/><stop offset="1" stop-color="#4e6a2a"/></linearGradient></defs>
    <circle cx="200" cy="200" r="174" fill="url(#meadow)" role="img" aria-label="Photo of a child praying in a sunlit meadow"/>
  </svg>
  <div class="down-btn" style="top:578px">&#8595;</div>
</section>

<section class="about">
  <h2>About me</h2>
  <span class="underline"></span>
  <div class="abs" role="img" aria-label="Photo of green mountains" style="left:0;top:222px;width:184px;height:318px;background:linear-gradient(180deg,#7db3e0 0%,#5d8a45 55%,#2f5a22 100%);border-radius:0 6px 6px 0"></div>
  <div class="abs" style="left:216px;top:578px;width:300px;height:200px;border:5px solid var(--orange);border-top:none;border-left:none;border-radius:0 0 8px 0"></div>
  <div class="abs" style="left:506px;top:574px;width:10px;height:5px;background:var(--orange)"></div>
  <div class="abs" role="img" aria-label="Photo of the founder smiling with arms crossed in an office" style="left:92px;top:280px;width:382px;height:436px;background:linear-gradient(160deg,#e6e8ea 0%,#c9ccd0 55%,#8d9197 100%);border-radius:6px;box-shadow:0 10px 30px rgba(0,0,0,.12)"></div>
  <div class="about-text">
    <p>Voluptatem accusantium doloremque laudantium, totam rem aperiam, eaque ipsa quae abist illo inventore veritatis et quasi architecto beatae vitae dictaphon sunt explicabo. Nemo enim ipsam voluptatem quia voluptas sit aspernatur auts onno.</p>
    <p>Neque porro quisquam est, qui dolorem ipsum quia dolor sit amet, consectetur, adipisci velit, sed quia non numquam eius modi tempora incidunt ut labore et dolore.</p>
  </div>
  <ul class="checks">
    <li><svg width="18" height="14" viewBox="0 0 18 14"><path d="M2 7l5 5L16 2" fill="none" stroke="var(--orange)" stroke-width="2.6"/></svg>More-or-less normal distribution of letters.</li>
    <li><svg width="18" height="14" viewBox="0 0 18 14"><path d="M2 7l5 5L16 2" fill="none" stroke="var(--orange)" stroke-width="2.6"/></svg>Various versions have evolved over the years</li>
    <li><svg width="18" height="14" viewBox="0 0 18 14"><path d="M2 7l5 5L16 2" fill="none" stroke="var(--orange)" stroke-width="2.6"/></svg>When an unknown printer took a galley</li>
  </ul>
  <a class="btn btn-blue" href="#">Read More
    <svg class="arrow-ic" viewBox="0 0 16 16" fill="none" stroke="#fff" stroke-width="1.6"><circle cx="8" cy="8" r="7"/><path d="M5 8h6M8.5 5.5 11 8l-2.5 2.5"/></svg></a>
</section>

<section class="purpose">
  <div class="purpose-band"></div>
  <h2>Our purpose</h2>
  <span class="underline"></span>
  <p class="purpose-lead">Voluptatem accusantium doloremque laudantium, totam rem aperiam eaque ipsa quae abist illo inventore veritatis et quasi architecto beatae vitae dictaphon sunt explicabo.</p>

  <div class="card" style="left:92px;top:234px">
    <svg class="ic" width="64" height="70" viewBox="0 0 64 70" fill="none" stroke="var(--blue)" stroke-width="2"><path d="M10 14 32 4l22 10-22 10z"/><circle cx="32" cy="32" r="9"/><rect x="6" y="44" width="52" height="22" rx="2"/><path d="M22 66V54h20v12"/></svg>
    <h3>School foundations</h3><span class="underline"></span>
    <p>Ut enim ad minim veniam uisop nostrud exercitation ullamcomosi laboris nisi ut aliquip.</p>
    <a class="btn btn-soft" href="#">Read More <svg class="arrow-ic" viewBox="0 0 16 16" fill="none" stroke="var(--blue)" stroke-width="1.6"><circle cx="8" cy="8" r="7"/><path d="M5 8h6M8.5 5.5 11 8l-2.5 2.5"/></svg></a>
  </div>
  <div class="card" style="left:436px;top:234px">
    <svg class="ic" width="64" height="70" viewBox="0 0 64 70" fill="none" stroke="var(--blue)" stroke-width="2"><ellipse cx="32" cy="35" rx="28" ry="11"/><ellipse cx="32" cy="35" rx="28" ry="11" transform="rotate(60 32 35)"/><ellipse cx="32" cy="35" rx="28" ry="11" transform="rotate(-60 32 35)"/><circle cx="32" cy="35" r="5" stroke="var(--orange)"/></svg>
    <h3>Curriculum</h3><span class="underline"></span>
    <p>Ut enim ad minim veniam uisop nostrud exercitation ullamcomosi laboris nisi ut aliquip.</p>
    <a class="btn btn-soft" href="#">Read More <svg class="arrow-ic" viewBox="0 0 16 16" fill="none" stroke="var(--blue)" stroke-width="1.6"><circle cx="8" cy="8" r="7"/><path d="M5 8h6M8.5 5.5 11 8l-2.5 2.5"/></svg></a>
  </div>
  <div class="card" style="left:780px;top:234px">
    <svg class="ic" width="64" height="70" viewBox="0 0 64 70" fill="none" stroke="var(--blue)" stroke-width="2"><rect x="6" y="22" width="44" height="40" rx="3"/><circle cx="20" cy="38" r="6"/><path d="M10 58c2-8 18-8 20 0"/><path d="M38 16a8 8 0 1 1 12 7v5h-8v-5a8 8 0 0 1-4-7z" stroke="var(--orange)"/><path d="M44 4v4M56 10l-3 3M32 10l3 3" stroke="var(--orange)"/></svg>
    <h3>Pedagogy</h3><span class="underline"></span>
    <p>Ut enim ad minim veniam uisop nostrud exercitation ullamcomosi laboris nisi ut aliquip.</p>
    <a class="btn btn-soft" href="#">Read More <svg class="arrow-ic" viewBox="0 0 16 16" fill="none" stroke="var(--blue)" stroke-width="1.6"><circle cx="8" cy="8" r="7"/><path d="M5 8h6M8.5 5.5 11 8l-2.5 2.5"/></svg></a>
  </div>

  <div class="card" style="left:92px;top:648px">
    <svg class="ic" width="64" height="70" viewBox="0 0 64 70" fill="none" stroke="var(--blue)" stroke-width="2"><circle cx="32" cy="12" r="6"/><path d="M14 22l18 6 18-6M32 28v20M24 64l8-16 8 16"/><path d="M8 64V46M4 50l4-4 4 4M56 64V40M52 44l4-4 4 4" stroke="var(--orange)"/></svg>
    <h3>Outcomes</h3><span class="underline"></span>
    <p>Ut enim ad minim veniam uisop nostrud exercitation ullamcomosi laboris nisi ut aliquip.</p>
    <a class="btn btn-soft" href="#">Read More <svg class="arrow-ic" viewBox="0 0 16 16" fill="none" stroke="var(--blue)" stroke-width="1.6"><circle cx="8" cy="8" r="7"/><path d="M5 8h6M8.5 5.5 11 8l-2.5 2.5"/></svg></a>
  </div>
  <div class="card" style="left:436px;top:648px">
    <svg class="ic" width="64" height="70" viewBox="0 0 64 70" fill="none" stroke="var(--blue)" stroke-width="2"><rect x="6" y="18" width="46" height="42" rx="3"/><path d="M14 34h20M14 42h24M14 50h16"/><path d="M40 22a8 8 0 1 1 12 7v4h-8v-4a8 8 0 0 1-4-7z" stroke="var(--orange)"/><path d="M46 6v4M58 12l-3 3" stroke="var(--orange)"/></svg>
    <h3>Opening</h3><span class="underline"></span>
    <p>Ut enim ad minim veniam uisop nostrud exercitation ullamcomosi laboris nisi ut aliquip.</p>
    <a class="btn btn-soft" href="#">Read More <svg class="arrow-ic" viewBox="0 0 16 16" fill="none" stroke="var(--blue)" stroke-width="1.6"><circle cx="8" cy="8" r="7"/><path d="M5 8h6M8.5 5.5 11 8l-2.5 2.5"/></svg></a>
  </div>
  <div class="card donate" style="left:780px;top:648px" role="img" aria-label="Photo of hands holding a red heart, with a donation call to action">
    <span class="corner" style="left:16px;top:16px;border-right:none;border-bottom:none;width:22px;height:44px"></span>
    <span class="abs" style="left:24px;top:70px;width:10px;height:10px;background:var(--orange)"></span>
    <span class="corner" style="right:16px;bottom:16px;border-left:none;border-top:none;width:22px;height:44px"></span>
    <span class="abs" style="right:24px;bottom:70px;width:10px;height:10px;background:var(--white)"></span>
    <div class="badge"><svg width="40" height="40" viewBox="0 0 40 40"><rect x="6" y="16" width="28" height="18" rx="2" fill="var(--blue)"/><circle cx="20" cy="10" r="6" fill="var(--orange)"/><path d="M20 30l-6-6a3.5 3.5 0 0 1 6-3 3.5 3.5 0 0 1 6 3z" fill="#fff"/></svg></div>
    <h3>For hold hands<br>together tight<br>donate us...</h3>
    <a class="btn btn-orange" href="#">Donate Now <svg class="arrow-ic" viewBox="0 0 16 16" fill="none" stroke="#fff" stroke-width="1.6"><circle cx="8" cy="8" r="7"/><path d="M5 8h6M8.5 5.5 11 8l-2.5 2.5"/></svg></a>
  </div>
</section>

<section class="statement">
  <h2>Statement of oneness with equity</h2>
  <span class="underline"></span>
  <p>Voluptatem accusantium doloremque laudantium, totam rem aperiam, eaque ipsa quae abist illo inventore veritatis et quasi architecto beatae vitae dictaphon sunt explicabo. Nemo enim ipsam voluptatem quia voluptas sit aspernatur auts onno.</p>
  <svg class="rings" width="1200" height="420" viewBox="0 0 1200 420">
    <defs>
      <linearGradient id="kids" x1="0" y1="0" x2="1" y2="1"><stop offset="0" stop-color="#e9d3c4"/><stop offset="1" stop-color="#c98a7a"/></linearGradient>
      <linearGradient id="flowers" x1="0" y1="0" x2="1" y2="1"><stop offset="0" stop-color="#5f7d3f"/><stop offset=".5" stop-color="#d77ca6"/><stop offset="1" stop-color="#3f5a2c"/></linearGradient>
      <linearGradient id="family" x1="0" y1="0" x2="1" y2="1"><stop offset="0" stop-color="#e0b46a"/><stop offset=".6" stop-color="#a4612f"/><stop offset="1" stop-color="#6c3d22"/></linearGradient>
    </defs>
    <path d="M96 112 A186 186 0 0 1 446 70" fill="none" stroke="var(--orange)" stroke-width="8"/>
    <path d="M754 70 A186 186 0 0 1 1104 112" fill="none" stroke="var(--orange)" stroke-width="8"/>
    <path d="M422 316 A186 186 0 0 0 778 316" fill="none" stroke="var(--blue)" stroke-width="8"/>
    <circle cx="266" cy="180" r="170" fill="url(#kids)" role="img" aria-label="Photo of three smiling children hugging"/>
    <circle cx="600" cy="170" r="170" fill="url(#flowers)" stroke="#fff" stroke-width="6" role="img" aria-label="Photo of pink blossoms on a branch"/>
    <circle cx="934" cy="180" r="170" fill="url(#family)" role="img" aria-label="Photo of a family with a toddler on a father's shoulders in autumn"/>
  </svg>
</section>

<section class="reviews">
  <h2>What our<br>learners says</h2>
  <span class="underline"></span>
  <div class="nav-arrows">
    <span style="background:#dde3ef"><svg width="20" height="20" viewBox="0 0 20 20" fill="none" stroke="var(--blue)" stroke-width="2"><path d="M16 10H4M9 5l-5 5 5 5"/></svg></span>
    <span style="background:var(--blue)"><svg width="20" height="20" viewBox="0 0 20 20" fill="none" stroke="#fff" stroke-width="2"><path d="M4 10h12M11 5l5 5-5 5"/></svg></span>
  </div>
  <div class="review" style="left:92px">
    <div class="avatar" role="img" aria-label="Portrait of a student" style="background:linear-gradient(135deg,#d9c2b6,#8a5a48)"></div>
    <svg class="quote" width="62" height="56" viewBox="0 0 62 56"><path d="M2 0h24v26q0 22-18 30l-4-8q10-6 10-18H2zM36 0h24v26q0 22-18 30l-4-8q10-6 10-18H36z" fill="var(--orange)"/></svg>
    <p>sed do eiusmod tempor incididunt ut labore etenis dolore magna aliqua. Ut enim ad minim veniam quis nostrud exercitation ullamcoinventore veritatis..</p>
    <div class="name">Maya Rivers</div><div class="role">Student</div>
  </div>
  <div class="review" style="left:614px">
    <div class="avatar" role="img" aria-label="Portrait of a student" style="background:linear-gradient(135deg,#e9cf6a,#9c5fa0)"></div>
    <svg class="quote" width="62" height="56" viewBox="0 0 62 56"><path d="M2 0h24v26q0 22-18 30l-4-8q10-6 10-18H2zM36 0h24v26q0 22-18 30l-4-8q10-6 10-18H36z" fill="var(--orange)"/></svg>
    <p>sed do eiusmod tempor incididunt ut labore etenis dolore magna aliqua. Ut enim ad minim veniam quis nostrud exercitation ullamcoinventore veritatis..</p>
    <div class="name">Clara Benton</div><div class="role">Student</div>
  </div>
</section>

<footer class="footer">
  <div class="foot-brand">Evergreen Unity School</div>
  <div class="foot-social" aria-label="Social links"><span></span><span></span><span></span></div>
  <h4 style="left:426px">Quick links</h4><span class="underline" style="left:426px"></span>
  <ul class="links" style="left:426px"><li>About</li><li>School Foundations</li><li>Curriculum</li><li>Pedagogy</li></ul>
  <ul class="links" style="left:632px"><li>Outcome</li><li>Opening</li><li>Testimonials</li><li>Donate</li></ul>
  <h4 style="left:882px">Contact info</h4><span class="underline" style="left:882px"></span>
  <div class="contact" style="top:144px">
    <svg class="ic" width="16" height="16" viewBox="0 0 24 24" fill="var(--orange)"><path d="M5 3h4l2 5-3 2a12 12 0 0 0 6 6l2-3 5 2v4a2 2 0 0 1-2 2A18 18 0 0 1 3 5a2 2 0 0 1 2-2z"/></svg>
    <div>Phone no:<br>123-456-7890</div>
  </div>
  <div class="contact" style="top:234px">
    <svg class="ic" width="18" height="16" viewBox="0 0 18 16"><path d="M1 7 9 1l8 6v8H1z" fill="var(--orange)"/></svg>
    <div>Email:<br>hello@evergreenunity.org</div>
  </div>
  <div class="copy">Copyright © 2023 Evergreen Unity School. All rights reserved.</div>
</footer>

</body>
</html>
```